Wakeboarding and Aqua Park front cover for flyer

I would like a front cover that I can use on a DL flyer to advertise both our Aqua Park and Cable Ski. The design should reflect the fun nature of our activity and appeal to both families and young people (18-30) but with may be a touch of an extreme sports feel.

I would like two pictures to be visible, one of the Aqua Park and the other the cable ski plus our logo. Both should have prominence but if the design has one at the top and the other at the bottom please put the Aqua Park at the top as this is currently our most popular activity.

There should be some text visible near the Aqua Park picture saying:

AQUA PARK
"Bigger and Better for 2017!"

There should be some text visible near/over the Cable Ski picture saying:

CABLE SKI
"Try kneeboarding, water skiing or wakeboarding this summer!"

Target Market(s)

Young people, families

Industry/Entity Type

Entertainment

Colors
0255a3
fbed22
fbee3e
0692cd

Requirements
Must have
• Picture of wakeboarding, picture of Aqua Park
Nice to have
• nice vibrant blues and yellows. illustration.
Should not have
• Have included a few extra aqua park images now in case they look better than the first one uploaded. Don't need to include them all though.

```html
<!DOCTYPE html>
<html lang="en">
<head>
<meta charset="utf-8">
<title>Riverside Cable Park – DL Flyer Covers</title>
<link rel="stylesheet" href="https://fonts.googleapis.com/css2?family=Anton&family=Kaushan+Script&family=Open+Sans:wght@700&display=swap">
<style>
  :root {
    --page-bg: #2f6f97;
    --deep-blue: #0a2f8f;
    --brand-blue: #0255a3;
    --bright-blue: #0692cd;
    --band-blue: #2a8ee0;
    --sky: #8cc8ef;
    --foam: #f4f9fc;
    --yellow: #fbed22;
    --orange: #f5a01e;
    --ink: #141414;
    --white: #ffffff;
  }
  * { box-sizing: border-box; margin: 0; padding: 0; }
  html, body { width: 1200px; height: 1200px; overflow: hidden; }
  body {
    background: radial-gradient(ellipse at 50% 40%, #3f86b0 0%, var(--page-bg) 60%, #245d84 100%);
    display: flex;
    align-items: center;
    justify-content: center;
    gap: 60px;
  }
  .flyer {
    position: relative;
    width: 420px;
    height: 880px;
    overflow: hidden;
    background: linear-gradient(180deg, var(--bright-blue) 0%, var(--brand-blue) 50%, var(--deep-blue) 100%);
    box-shadow: 0 14px 34px rgba(0, 20, 60, 0.4);
  }
  .flyer__photo {
    position: absolute;
    inset: 0 0 auto 0;
    width: 420px;
    height: 500px;
  }
  .flyer__brand {
    position: absolute;
    top: 30px;
    left: 0;
    right: 0;
    display: flex;
    align-items: center;
    justify-content: center;
    gap: 10px;
    font-family: "Anton", sans-serif;
    font-size: 30px;
    letter-spacing: 0.5px;
    color: var(--white);
    text-transform: lowercase;
    line-height: 1;
  }
  .flyer__brand-dot {
    width: 22px; height: 22px;
    border-radius: 50%;
    background: var(--white);
  }
  .flyer__headline {
    position: absolute;
    left: 0; right: 0;
    top: 505px;
    text-align: center;
    font-family: "Anton", sans-serif;
    font-weight: 400;
    text-transform: uppercase;
    line-height: 0.98;
    color: var(--white);
    text-shadow:
      3px 0 0 var(--ink), -3px 0 0 var(--ink), 0 3px 0 var(--ink), 0 -3px 0 var(--ink),
      2px 2px 0 var(--ink), -2px -2px 0 var(--ink), 2px -2px 0 var(--ink), -2px 2px 0 var(--ink);
  }
  .flyer__kicker {
    display: block;
    color: var(--orange);
    font-size: 36px;
    margin-bottom: 6px;
  }
  .flyer__big { display: block; font-size: 100px; }
  .flyer__mid { display: block; font-size: 60px; }
  .flyer__year { display: block; color: var(--orange); font-size: 40px; text-align: right; padding-right: 56px; margin-top: 8px; }
  .flyer__line { display: block; font-size: 42px; }
  .flyer__script {
    display: block;
    font-family: "Kaushan Script", cursive;
    text-transform: none;
    color: var(--orange);
    font-size: 34px;
    line-height: 1.1;
    text-align: right;
    padding-right: 40px;
    margin-top: 4px;
  }
  .flyer__footer {
    position: absolute;
    left: 0; right: 0; bottom: 0;
    height: 56px;
    background: var(--band-blue);
    display: flex;
    align-items: center;
    justify-content: center;
    font-family: "Open Sans", sans-serif;
    font-weight: 700;
    font-size: 17px;
    color: var(--white);
  }
</style>
</head>
<body>

  <section class="flyer flyer--aqua-park">
    <svg class="flyer__photo" viewBox="0 0 420 500" role="img" aria-label="Photo of friends in life jackets sliding down a white inflatable aqua park slide into splashing lake water under a blue sky">
      <defs>
        <linearGradient id="aquaSky" x1="0" y1="0" x2="0" y2="1">
          <stop offset="0" stop-color="#3f9ddc"/>
          <stop offset="0.45" stop-color="#9fd2f0"/>
          <stop offset="0.7" stop-color="#5aa7d8"/>
          <stop offset="1" stop-color="#1d6fc0"/>
        </linearGradient>
        <radialGradient id="aquaSlide" cx="0.3" cy="0.45" r="0.45">
          <stop offset="0" stop-color="#ffffff" stop-opacity="0.95"/>
          <stop offset="0.6" stop-color="#e6f1f8" stop-opacity="0.6"/>
          <stop offset="1" stop-color="#e6f1f8" stop-opacity="0"/>
        </radialGradient>
        <radialGradient id="aquaRiders" cx="0.58" cy="0.5" r="0.3">
          <stop offset="0" stop-color="#2b5fae" stop-opacity="0.75"/>
          <stop offset="0.55" stop-color="#d9c25a" stop-opacity="0.35"/>
          <stop offset="1" stop-color="#d9c25a" stop-opacity="0"/>
        </radialGradient>
        <linearGradient id="aquaFade" x1="0" y1="0" x2="0" y2="1">
          <stop offset="0" stop-color="#0255a3" stop-opacity="0"/>
          <stop offset="1" stop-color="#0255a3" stop-opacity="1"/>
        </linearGradient>
      </defs>
      <rect width="420" height="500" fill="url(#aquaSky)"/>
      <rect width="420" height="500" fill="url(#aquaSlide)"/>
      <rect width="420" height="500" fill="url(#aquaRiders)"/>
      <path d="M0 330 C 70 300, 140 360, 220 325 S 360 290, 420 320 L420 410 C 330 440, 230 395, 140 425 S 40 420, 0 400 Z" fill="var(--foam)" opacity="0.9"/>
      <path d="M0 385 C 90 360, 180 410, 280 380 S 390 370, 420 385 L420 500 L0 500 Z" fill="url(#aquaFade)"/>
    </svg>
    <div class="flyer__brand"><span class="flyer__brand-dot"></span>riverside cable park</div>
    <h2 class="flyer__headline">
      <span class="flyer__kicker">Aqua Park</span>
      <span class="flyer__big">Bigger</span>
      <span class="flyer__mid">And Better</span>
      <span class="flyer__year">For 2017</span>
    </h2>
    <div class="flyer__footer">www.riversidecablepark.com</div>
  </section>

  <section class="flyer flyer--cable-ski">
    <svg class="flyer__photo" viewBox="0 0 420 500" role="img" aria-label="Photo of a wakeboarder in a helmet carving across a tree-lined lake behind a cable tow, throwing up white spray">
      <defs>
        <linearGradient id="cableScene" x1="0" y1="0" x2="0" y2="1">
          <stop offset="0" stop-color="#4fa6e2"/>
          <stop offset="0.18" stop-color="#a7d5f0"/>
          <stop offset="0.28" stop-color="#6f9c68"/>
          <stop offset="0.36" stop-color="#4d8fa8"/>
          <stop offset="0.6" stop-color="#4a9ed6"/>
          <stop offset="1" stop-color="#1d6fc0"/>
        </linearGradient>
        <radialGradient id="cableRider" cx="0.4" cy="0.45" r="0.32">
          <stop offset="0" stop-color="#1f3f86" stop-opacity="0.85"/>
          <stop offset="0.5" stop-color="#e08a3a" stop-opacity="0.3"/>
          <stop offset="1" stop-color="#e08a3a" stop-opacity="0"/>
        </radialGradient>
        <linearGradient id="cableFade" x1="0" y1="0" x2="0" y2="1">
          <stop offset="0" stop-color="#0255a3" stop-opacity="0"/>
          <stop offset="1" stop-color="#0255a3" stop-opacity="1"/>
        </linearGradient>
      </defs>
      <rect width="420" height="500" fill="url(#cableScene)"/>
      <rect width="420" height="500" fill="url(#cableRider)"/>
      <path d="M0 300 C 80 330, 160 290, 250 320 S 370 300, 420 280 L420 410 C 330 440, 230 395, 140 425 S 40 420, 0 400 Z" fill="var(--foam)" opacity="0.9"/>
      <path d="M0 385 C 90 360, 180 410, 280 380 S 390 370, 420 385 L420 500 L0 500 Z" fill="url(#cableFade)"/>
    </svg>
    <div class="flyer__brand"><span class="flyer__brand-dot"></span>riverside cable park</div>
    <h2 class="flyer__headline">
      <span class="flyer__kicker">Cable Ski</span>
      <span class="flyer__line">Try kneeboarding,</span>
      <span class="flyer__line">water skiing or</span>
      <span class="flyer__line">wakeboarding</span>
      <span class="flyer__script">this summer!</span>
    </h2>
    <div class="flyer__footer">www.riversidecablepark.com</div>
  </section>

</body>
</html>
```